Letterhead for SaaS

Design a letterhead that aligns with our new business card, using our logo and color scheme and text defined in the Branding Guide to ensure consistency. Consider incorporating a subtle watermark for added elegance. The layout should reflect the card's style, creating a cohesive look across our stationery.

```html
<!DOCTYPE html>
<html lang="en">
<head>
<meta charset="utf-8">
<title>Vanteris Letterhead</title>
<link href="https://fonts.googleapis.com/css2?family=Arimo:wght@400;700&display=swap" rel="stylesheet">
<style>
  :root {
    --ink-navy: #121a28;
    --paper: #f6f3f4;
    --text: #3c3c3e;
    --text-soft: #4a4a4c;
    --mark-faint: #e4e2e4;
    --white: #ffffff;
  }
  * { margin: 0; padding: 0; box-sizing: border-box; }
  html, body { width: 942px; height: 1200px; overflow: hidden; background: var(--paper); }
  body { font-family: "Arimo", Arial, sans-serif; color: var(--text); }

  .letterhead { position: relative; width: 942px; height: 1200px; background: var(--paper); }

  .header-band { position: absolute; left: 0; top: 0; width: 942px; height: 200px; }

  .brand-name {
    position: absolute; left: 81px; top: 150px;
    font-weight: 700; font-size: 27px; letter-spacing: 0.5px;
    color: var(--white);
  }

  .contact {
    position: absolute; right: 62px; top: 82px;
    list-style: none; text-align: right;
    font-size: 15px; line-height: 19px; color: #1f1f22;
  }
  .contact li { display: flex; justify-content: flex-end; align-items: center; gap: 6px; }
  .contact svg { width: 13px; height: 13px; fill: #1f1f22; }

  .watermark { position: absolute; left: 280px; top: 250px; }

  .letter-body { position: absolute; left: 64px; top: 282px; width: 816px; }
  .salutation { font-size: 26px; font-weight: 400; color: var(--text-soft); margin-bottom: 42px; }
  .letter-body p.copy {
    font-size: 14px; line-height: 20px; text-align: justify; hyphens: auto;
    margin-bottom: 20px; color: var(--text);
  }
  .closing { font-size: 14px; margin-top: 32px; }

  .signature { position: absolute; left: 72px; top: 872px; }
  .signatory { position: absolute; left: 77px; top: 940px; }
  .signatory-name { font-size: 19px; color: var(--text-soft); }
  .signatory-role { font-size: 15px; margin-top: 6px; color: var(--text-soft); }
</style>
</head>
<body>
<main class="letterhead">

  <svg class="header-band" viewBox="0 0 942 200" aria-hidden="true">
    <polygon points="0,21 367,21 259,193 0,193" fill="var(--ink-navy)"/>
    <circle cx="112" cy="100" r="34" fill="#2a3446"/>
  </svg>
  <div class="brand-name">VANTERIS</div>

  <ul class="contact">
    <li>(555) 014-2290
      <svg viewBox="0 0 16 16" aria-hidden="true"><path d="M3.6 1.2l2.3 2.9-1.4 1.7c.9 2 2.7 3.8 4.7 4.7l1.7-1.4 2.9 2.3-1.3 2.6C7.5 14.2 1.8 8.5 1 3.5z"/></svg>
    </li>
    <li>maren.l@vanteris.com
      <svg viewBox="0 0 16 16" aria-hidden="true"><path d="M1 3h14v10H1z M2.2 4.2L8 8.6l5.8-4.4z" fill-rule="evenodd"/></svg>
    </li>
    <li>www.vanteris.com
      <svg viewBox="0 0 16 16" aria-hidden="true"><circle cx="8" cy="8" r="7"/><path d="M4 5c2 0 2 2 4 2s1 3 3 3" stroke="#f6f3f4" stroke-width="1.4" fill="none"/></svg>
    </li>
  </ul>

  <svg class="watermark" width="330" height="690" viewBox="0 0 330 690" role="img" aria-label="Faint brand watermark">
    <circle cx="165" cy="300" r="160" fill="var(--mark-faint)" opacity="0.7"/>
  </svg>

  <section class="letter-body">
    <h1 class="salutation">Dear Mr. Hollis,</h1>
    <p class="copy">Lorem ipsum dolor sit amet, consectetur adipiscing elit. Donec orci purus, luctus vitae dignissim eu, iaculis sed purus. Vivamus faucibus, ipsum nec aliquet viverra, leo mauris condimentum ligula, sit amet sagittis enim ligula quis arcu. Nam egestas tortor id nisi porttitor mattis. In tortor ante, ultricies in suscipit a, tempus non massa. Vivamus et auctor mi. Fusce vel massa nulla. Phasellus nec eros mauris, et scelerisque orci.</p>
    <p class="copy">Donec malesuada orci vitae nulla accumsan porta a id massa. Quisque accumsan iaculis magna sit amet fringilla. Maecenas consequat, magna eget tincidunt semper, odio nibh rutrum mi, id feugiat ante nisi eu risus. Vestibulum nunc orci, rhoncus a placerat in, ultricies in mi. Cras mattis varius eros, vel fringilla nisi suscipit eget. Quisque scelerisque sagittis nulla at porttitor.</p>
    <p class="copy">Sed id augue vitae urna euismod commodo aliquet a quam. Pellentesque arcu velit, cursus et malesuada ut, consequat et diam. Nullam erat sem, rhoncus id ullamcorper vitae, rhoncus et arcu. In ultricies ultricies nulla, ut rutrum nisi iaculis at. Donec eu magna a metus ornare faucibus. Fusce aliquet faucibus ultricies. Morbi semper, est id tincidunt gravida, sem arcu adipiscing lacus, ac bibendum nulla leo eu purus. Quisque nec diam sed risus consectetur a ccumsan quis quis nibh. Vestibulum id purus lorem.</p>
    <p class="copy">It is a long established fact that a reader will be distracted by the readable content of a page when looking at its layout. The point of using Lorem Ipsum is that it has a more-or-less normal distribution of letters, as opposed to using 'Content here, content here', making it look like readable English. Many desktop publishing packages</p>
    <p class="closing">Sincerely,</p>
  </section>

  <svg class="signature" width="130" height="52" viewBox="0 0 130 52" role="img" aria-label="Handwritten signature">
    <rect x="0" y="14" width="120" height="26" rx="13" fill="#d9d8dc"/>
  </svg>

  <div class="signatory">
    <p class="signatory-name">Daniel Hollis</p>
    <p class="signatory-role">CEO/ Founder</p>
  </div>

</main>
</body>
</html>
```